Nonprofit serving disconnected/homeless young adults (age 18-24) needs marketing

There are over 5 Million young adults in the U.S. who are neither working nor in school. Many of them 'aged out' of foster care or group homes, meaning the state doesn't provide care for them when they become an adult at age 18. These young adults have slipped through the cracks of society. Many are homeless, which often times leads to drug use, crime, young pregnancy, violence and prison. VANTA is a nonprofit dedicated to providing young adults opportunities, resources and experiences to begin building a life they value. We do that via two channels: one our 6-month living program, where participants live expense-free. The requirement is they work full-time, and save at least 75% of their income. At the end of the 6 months, they have the money needed to get into their own place, along with starter furniture and household basics. All potential candidates for housing program come from the resource center VANTALink. It's where VANTA offers immediate assistance to young adults, and in-turn we get to know them, and them us. This is essential to see if they're a fit for the housing program. The marketing piece is something young adults (and members of the community) receive. It should 1) be eye catching, maybe something like a path or a road with a phrase "have you chosen the path you're on?" "if given the chance, would you choose something different?" "this is your opportunity to get serious about what matters most to you" "want something different for you life, here's your chance" ...something to that effect. I want the graphics to be big, in your face, something eye catching.

After that, something that says: "here's how"
1. EVERYTHING IN LIFE STARTS WITH THE FIRST STEP: attend orientation on Tuesday if you haven't already
2. YOU WANT TO SOMETHING DIFFERENT FOR YOUR LIFE, YOU NEED TO DO SOMETHING DIFFERENT: our classes are it.
3. YOU WANT TO BE SUCCESSFUL? HANG OUT WITH LIKE-MINDED INDIVIDUALS: attend a volunteer day or fun activity.

(I uploaded our Logo and our new t-shirt design so you can get a look/feel of our current marketing. it should be somewhat modern, "cool" because we're talking to young adults and again - modern design with large graphics.)

Industry/Entity Type

School

```html
<!DOCTYPE html>
<html lang="en">
<head>
<meta charset="utf-8">
<title>VANTA – Have You Chosen the Path You're On?</title>
<link rel="stylesheet" href="https://fonts.googleapis.com/css2?family=Bree+Serif&family=Kaushan+Script&family=Covered+By+Your+Grace&family=Ubuntu:wght@500;700&family=Montserrat:wght@800&display=swap">
<style>
  :root {
    --concrete: #ececec;
    --road-green: #2cb34d;
    --accent-green: #3cb54a;
    --ink: #1c1c1c;
    --badge-grey: #e3e3e5;
    --bubble-brown: #231512;
    --white: #ffffff;
    --teal: #1f9b8f;
  }
  * { margin: 0; padding: 0; box-sizing: border-box; }
  html, body { width: 927px; height: 1200px; overflow: hidden; background: var(--concrete); }
  .flyer { position: relative; width: 927px; height: 1200px; background: var(--concrete); overflow: hidden; }
  .chalk-strokes {
    position: absolute; left: 0; top: 320px; width: 927px; height: 600px;
    background:
      linear-gradient(180deg, rgba(236,236,236,0) 0%, rgba(240,190,180,.45) 12%, rgba(180,205,230,.5) 28%,
      rgba(240,225,160,.45) 45%, rgba(185,220,180,.45) 60%, rgba(180,205,230,.45) 75%, rgba(236,236,236,0) 100%);
  }
  .art { position: absolute; left: 0; top: 0; }
  .badge-text { position: absolute; color: var(--ink); line-height: 1; }
  .badge-have { left: 462px; top: 166px; font: 44px "Bree Serif", serif; letter-spacing: 1px; }
  .badge-you { left: 428px; top: 206px; font: 62px "Bree Serif", serif; }
  .badge-chosen { left: 300px; top: 228px; font: 96px "Kaushan Script", cursive; letter-spacing: -2px; }
  .badge-path { left: 362px; top: 330px; font: 42px "Bree Serif", serif; }
  .badge-on { left: 363px; top: 372px; font: 38px "Bree Serif", serif; }
  .intro {
    position: absolute; left: 133px; top: 540px; width: 790px;
    font: 700 19px/23px "Ubuntu", sans-serif; color: var(--ink);
  }
  .step { position: absolute; left: 470px; width: 380px; }
  .step-lead { font: 32px/31px "Covered By Your Grace", cursive; color: var(--ink); }
  .step-action { width: 320px; margin-top: 4px; font: 700 19px/25px "Ubuntu", sans-serif; color: var(--accent-green); text-transform: uppercase; letter-spacing: .5px; }
  .step-classes { top: 652px; }
  .step-friends { top: 798px; }
  .bubble-text { position: absolute; left: 150px; top: 786px; width: 220px; font: 17px/23px "Ubuntu", sans-serif; }
  .bubble-lead { color: var(--white); font-weight: 700; text-transform: uppercase; }
  .bubble-action { color: var(--accent-green); font-weight: 500; }
  .register { position: absolute; left: 133px; top: 1075px; font: 800 36px "Montserrat", sans-serif; letter-spacing: 7px; color: var(--accent-green); }
  .phone { position: absolute; left: 133px; top: 1118px; display: flex; align-items: center; gap: 6px; font: 700 27px "Ubuntu", sans-serif; color: var(--ink); }
  .brand { position: absolute; left: 540px; top: 1010px; display: flex; align-items: center; gap: 16px; }
  .brand-square { width: 80px; height: 80px; background: var(--teal); }
  .brand-name { font: 700 64px "Ubuntu", sans-serif; color: var(--teal); letter-spacing: 2px; }
  .tagline { position: absolute; left: 510px; top: 1124px; font: 500 10px "Ubuntu", sans-serif; color: var(--teal); letter-spacing: 1px; }
</style>
</head>
<body>
<main class="flyer">
  <div class="chalk-strokes" role="img" aria-label="Pastel chalk strokes scribbled across concrete"></div>

  <svg class="art" width="927" height="520" viewBox="0 0 927 520" aria-hidden="true">
    <rect x="358" y="0" width="211" height="112" fill="var(--road-green)"/>
    <rect x="460" y="0" width="5" height="60" fill="var(--white)"/>
    <rect x="0" y="110" width="927" height="210" fill="var(--road-green)"/>
    <g fill="var(--white)">
      <rect x="4" y="214" width="52" height="5"/>
      <rect x="150" y="214" width="90" height="5"/>
      <rect x="690" y="214" width="72" height="5"/>
      <rect x="785" y="214" width="95" height="5"/>
    </g>
    <defs><clipPath id="badge-clip"><circle cx="450" cy="310" r="195"/></clipPath></defs>
    <circle cx="450" cy="310" r="195" fill="var(--badge-grey)"/>
    <rect x="250" y="424" width="400" height="100" fill="var(--ink)" clip-path="url(#badge-clip)"/>
  </svg>

  <div class="badge-text badge-have">HAVE</div>
  <div class="badge-text badge-you">YOU</div>
  <div class="badge-text badge-chosen">Chosen</div>
  <div class="badge-text badge-path">the path</div>
  <div class="badge-text badge-on">you're on?</div>

  <p class="intro">if given the chance, would you choose something different? This is your opportunity to get serious about what matters most to you. want something different for you life, here's your chance!</p>

  <section class="step step-classes">
    <p class="step-lead">You want something different for your life, you need to do something different:</p>
    <p class="step-action">Our classes are it!</p>
  </section>
  <section class="step step-friends">
    <p class="step-lead">You want to be successful? Hang out with like-minded individuals:</p>
    <p class="step-action">Attend a volunteer or fun activity!</p>
  </section>

  <svg class="art" width="927" height="1200" viewBox="0 0 927 1200" aria-hidden="true">
    <ellipse cx="255" cy="850" rx="168" ry="118" fill="var(--bubble-brown)"/>
    <path d="M330 930 L412 1062 L290 955 Z" fill="var(--bubble-brown)"/>
  </svg>
  <div class="bubble-text">
    <p class="bubble-lead">Everything in life starts with the first step:</p>
    <p class="bubble-action">Attend orientation on Tuesday if you haven't already.</p>
  </div>

  <div class="register">REGISTER</div>
  <div class="phone">
    <svg width="22" height="22" viewBox="0 0 22 22" aria-hidden="true">
      <circle cx="11" cy="11" r="9.5" fill="none" stroke="var(--ink)" stroke-width="1.6"/>
      <path d="M8 6 Q6 8 8 12 Q10 16 14 16 L15 14 L13 12.5 L12 13.5 Q10 12 9.5 10 L10.5 9 L9.5 6.5 Z" fill="var(--ink)"/>
    </svg>
    <span>0123.555.0142</span>
  </div>

  <div class="brand">
    <div class="brand-square"></div>
    <div class="brand-name">VANTA</div>
  </div>
  <p class="tagline">Vision. Action. New starts. Trust. Ambition.</p>
</main>
</body>
</html>
```